" Nome da empresa: Recanto Vivale CLINICA DE NUTRIÇAO SOMOS NUTRICIONISTAS E DESEJAMOS PROPORCIONAR AOS NOSSOS PACIENTES UM TRATAMENTO INDIVIDUALIZADO. FAREMOS ATENDIMENTOS NUTRICIONAIS A FIM DE LEVAR QUALIDADE DE VIDA E PREVENÇAO de doenças, focando na educaçao nutricional "

```html
<!DOCTYPE html>
<html lang="pt-BR">
<head>
<meta charset="utf-8">
<title>Recanto Vivale — Cartão de Visita</title>
<link rel="stylesheet" href="https://fonts.googleapis.com/css2?family=Arimo:ital,wght@0,400;1,400&family=Questrial&display=swap">
<style>
  :root {
    --backdrop: #ecebe7;
    --paper: #ffffff;
    --teal: #1f5b4f;
    --teal-text: #2b7466;
    --orange: #f0902c;
    --ink: #4a4a4a;
    --ink-soft: #6b6b6b;
    --white: #ffffff;
  }
  * { box-sizing: border-box; margin: 0; padding: 0; }
  html, body {
    width: 1200px; height: 1200px; overflow: hidden;
    background: var(--backdrop);
  }
  .canvas { position: relative; width: 1200px; height: 1200px; }
  .card {
    position: absolute;
    width: 660px; height: 400px;
    border-radius: 30px;
    overflow: hidden;
    box-shadow: 0 6px 18px rgba(0,0,0,0.18);
    font-family: "Arimo", Arial, sans-serif;
  }
  .card--front { left: 262px; top: 160px; background: var(--paper); color: var(--ink); }
  .card--back { left: 290px; top: 640px; background: var(--teal); color: var(--white); }

  .brand {
    position: absolute; right: 46px; top: 54px;
    display: flex; align-items: center; gap: 10px;
    font-family: "Questrial", Arial, sans-serif;
    font-size: 34px; letter-spacing: 0.2px;
  }
  .brand__dot { width: 14px; height: 14px; border-radius: 50%; background: var(--orange); }
  .card--front .brand__name { color: var(--teal-text); }
  .card--back .brand__name { color: var(--white); }

  .person { position: absolute; left: 34px; top: 140px; }
  .person__name { font-size: 25px; line-height: 1.1; }
  .person__role {
    font-style: italic; font-size: 14px; color: var(--orange);
    margin-left: 62px; margin-top: 2px;
  }
  .card--front .person__name { color: var(--ink); }

  .accent-bar {
    position: absolute; left: 0; top: 220px;
    width: 9px; height: 96px; background: var(--orange);
  }

  .contact {
    position: absolute; left: 92px; top: 232px;
    list-style: none; font-size: 11.5px; line-height: 1.7;
  }
  .card--front .contact { color: var(--ink-soft); }
  .contact__address { margin-top: 8px; line-height: 1.35; }
</style>
</head>
<body>
<main class="canvas">

  <section class="card card--front" aria-label="Frente do cartão">
    <div class="brand">
      <span class="brand__dot"></span>
      <span class="brand__name">Recanto Vivale</span>
    </div>
    <div class="person">
      <p class="person__name">Nome Sobrenome</p>
      <p class="person__role">Função</p>
    </div>
    <span class="accent-bar"></span>
    <ul class="contact">
      <li>Tel:0000-0000</li>
      <li>Cel:0000-0000</li>
      <li>Email:contato@recantovivale.com.br</li>
      <li class="contact__address">Endereço Rua das Flores,00 Bairro<br>Jardins, Cidade das Flores</li>
    </ul>
  </section>

  <section class="card card--back" aria-label="Verso do cartão">
    <div class="brand">
      <span class="brand__dot"></span>
      <span class="brand__name">Recanto Vivale</span>
    </div>
    <div class="person">
      <p class="person__name">Nome Sobrenome</p>
      <p class="person__role">Função</p>
    </div>
    <span class="accent-bar"></span>
    <ul class="contact">
      <li>Tel:0000-0000</li>
      <li>Cel:0000-0000</li>
      <li>Email:contato@recantovivale.com.br</li>
      <li class="contact__address">Endereço Rua das Flores,00 Bairro<br>Jardins, Cidade das Flores</li>
    </ul>
  </section>

</main>
</body>
</html>
```